Poem Handwritten by Veteran while in the jungle of Vietnam

My parents are celebrating their 50th wedding anniversary this year. I wanted to give them a very memorable gift. On my parents 2nd anniversary, my father was stationed in Vietnam. On that night he was in the jungle waiting till morning and wrote a poem to my mother using his pant leg as paper. I would like this poem to typographically designed to be framed and hung on the wall.

I have attached a picture of the poem below. It will need to be 11x14 when printed for framing. It would be great if there was background or artwork to make it more visually interesting, perhaps in a watercolor. My parents have a transitional style. I have attached some possible color schemes as well. Cool greens, blue, neutral grays, with hints of berries or highlights of yellow. These are just a guide, I would be open to your interpretations.

Thank you for your help. This will hopefully be a gift they will truly treasure as much as the poem itself.

Target Market(s)

My parents who are excited to be celebrating their 50th wedding anniversary. It should have a transitional, mature style.

Font styles to use
Serif
Script

Requirements
Must have
• The poem, typographically designed. There can be a mix of fonts, but legibility is critically important.
• Now that some designs have come through I wanted to give some more guidance of what I'm looking for. I want something that feels sophisticated and artistic.
Nice to have
• A background or art work, using the color schemes attached as a guide. I am really liking the designs that have a full color landscape artwork in the background. The fonts should be elegant and formal. I really like the romantic, muted colors. I had trouble finding similar projects online in the style I wanted until I cam across wedding invites. Those seem to be the most applicable. I've added pictures of some so you can get a sense of what I'm looking for. I am really liking the jungle foliage, starry skies or sunrises.
Should not have
• Cartoon caricatures, fonts that are too illegible when printed. I'm not liking anything whimsical. I don't like the very bright colors for this project.

```html
<!DOCTYPE html>
<html lang="en">
<head>
<meta charset="utf-8">
<title>Walter's Anniversary Poem</title>
<link rel="stylesheet" href="https://fonts.googleapis.com/css2?family=EB+Garamond:ital,wght@0,400;1,400&family=Montserrat:wght@400&family=Satisfy&display=swap">
<style>
  :root {
    --backdrop: #e6e9ee;
    --ink: #3e4650;
    --title-teal: #4d7c7a;
    --title-dark: #2f3140;
    --panel-fill: rgba(255, 255, 255, 0.5);
    --frame-line: #ffffff;
    --sky-gold: #f6c764;
    --sky-peach: #f3d9b6;
    --sky-violet: #8c88b4;
    --sky-slate: #6f7fa2;
    --mist: #c9d6cf;
    --jungle: #5f8f3c;
    --jungle-deep: #2f5a22;
  }
  * { box-sizing: border-box; margin: 0; padding: 0; }
  html, body { width: 1200px; height: 1000px; overflow: hidden; }
  body { background: var(--backdrop); position: relative; }

  .print {
    position: absolute;
    left: 230px; top: 30px;
    width: 740px; height: 940px;
    overflow: hidden;
  }
  .landscape {
    position: absolute; inset: 0;
    background:
      radial-gradient(ellipse 55% 22% at 55% 30%, rgba(255,214,110,0.95), rgba(246,199,100,0) 70%),
      linear-gradient(180deg,
        var(--sky-slate) 0%,
        var(--sky-peach) 14%,
        var(--sky-gold) 28%,
        var(--sky-violet) 44%,
        var(--mist) 60%,
        var(--jungle) 78%,
        var(--jungle-deep) 100%);
  }

  .title {
    position: absolute; left: 0; right: 0; top: 38px;
    text-align: center;
    font-weight: 400;
  }
  .title-name {
    display: block;
    font-family: "Satisfy", cursive;
    font-weight: 400;
    font-size: 62px; line-height: 1;
    color: var(--title-teal);
  }
  .title-word {
    display: block;
    font-family: "Montserrat", sans-serif;
    font-weight: 400;
    font-size: 36px; letter-spacing: 3px; line-height: 1;
    color: var(--title-dark);
    margin-top: -8px;
  }
  .title-sub {
    display: block;
    font-family: "Satisfy", cursive;
    font-weight: 400;
    font-size: 48px; line-height: 1;
    color: var(--title-teal);
    margin-top: -6px;
  }

  .frames { position: absolute; left: 0; top: 0; width: 740px; height: 940px; }

  .poem {
    position: absolute;
    left: 88px; top: 238px; width: 570px;
    display: flex; justify-content: space-between;
    font-family: "EB Garamond", serif;
    font-size: 13.6px; line-height: 17.4px;
    color: var(--ink);
    text-align: center;
  }
  .poem-column { width: 282px; }
  .stanza { margin-bottom: 17.4px; }
  .drop-cap {
    font-family: "Satisfy", cursive;
    font-size: 26px; line-height: 0;
    color: var(--title-teal);
  }
  .rule {
    width: 36px; height: 1px; background: var(--ink);
    margin: 6px auto; opacity: 0.6;
  }
  .note {
    font-style: italic;
    font-size: 9.5px; line-height: 12px;
    opacity: 0.85;
  }
</style>
</head>
<body>
  <main class="print">
    <div class="landscape" role="img" aria-label="Watercolor-style landscape of a sunrise glowing through clouds over a misty jungle of green foliage"></div>

    <h1 class="title">
      <span class="title-name">Walter's</span>
      <span class="title-word">ANNIVERSARY</span>
      <span class="title-sub">poem</span>
    </h1>

    <svg class="frames" viewBox="0 0 740 940" aria-hidden="true">
      <polygon points="72,198 370,222 668,190 664,818 76,822" fill="var(--panel-fill)"/>
      <polygon points="72,198 370,222 668,190 664,818 76,822" fill="none" stroke="var(--frame-line)" stroke-width="2"/>
      <polygon points="82,188 370,214 676,200 660,812 68,806" fill="none" stroke="var(--frame-line)" stroke-width="1.5"/>
    </svg>

    <section class="poem">
      <div class="poem-column">
        <p class="stanza"><span class="drop-cap">T</span>he trail began in the darkness,<br>A pathway of mud and of rain.<br>I walked it with you in my heart, dear,<br>And carried your name through the pain.</p>
        <p class="stanza">From the hush of the morning it wandered,<br>Through thickets of bramble and vine.<br>The hours were long in their passing,<br>Yet your promise was steady as mine.</p>
        <p class="stanza">The night settled close on the hillside,<br>The stars hid away in the haze.<br>I thought of the day that we married,<br>The start of our beautiful days.</p>
        <p class="stanza">Though the silence was heavy around me,<br>Your laughter was clear in my ear.<br>The miles could not keep us divided,<br>For always I felt you were near.</p>
        <p class="stanza">I met you, my Dearest, in springtime,<br>So gentle and bright was your smile.<br>Each moment beside you was golden,<br>Each hour worth more than a mile.</p>
        <p class="stanza">And now as I wait for the sunrise,<br>I write what my heart longs to say —<br>That love is the light on my journey,<br>And guides me back home on my way.</p>
      </div>
      <div class="poem-column">
        <p class="stanza">I pray for the end of this season,<br>The road that will lead me to you.<br>With patience and hope I keep waiting,<br>For I know that our love will stay true.</p>
        <p class="stanza">I count every day on my fingers,<br>I whisper your name to the trees.<br>Though the jungle is dark all around me,<br>Your love is the cool morning breeze.</p>
        <p class="stanza">Someday I will stand at our doorway,<br>So eager, so grateful, so glad!<br>I'll hold you again in the lamplight,<br>And cherish the years we have had.</p>
        <p class="stanza">What joy will be ours in tomorrow,<br>As side by side we grow old.<br>To treasure and honor each other,<br>Our story of love to be told.</p>
        <p class="stanza">I love you, my Darling, forever,<br>My heart is forever your own.<br>Wherever the pathway may take me,<br>With you I am never alone.</p>
        <div class="rule"></div>
        <p class="note">These verses were set down by moonlight<br>on a quiet watch far from home.<br>Written for our second anniversary,<br>on the only paper at hand,<br>and kept ever since.</p>
        <div class="rule"></div>
      </div>
    </section>
  </main>
</body>
</html>
```